Flyer Template

I need a flyer template for door knocking on properties. Text Boxes need to be editable, with a header and text body. Footer to be my info. Project to be stylized to match my real estate signs and logo art from past projects

```html
<!DOCTYPE html>
<html lang="en">
<head>
<meta charset="utf-8">
<title>Keston Realty – Door Knocking Flyer</title>
<link rel="stylesheet" href="https://fonts.googleapis.com/css2?family=Montserrat:wght@600;700;800&family=Open+Sans:wght@400;600&display=swap">
<style>
  :root {
    --brand-red: #e8303a;
    --brand-red-deep: #c81f2a;
    --ink: #0b0b0c;
    --paper: #ffffff;
    --white: #ffffff;
    --photo-red-light: #f0545b;
    --photo-red-dark: #a9161f;
    --sky-top: #6f87a6;
    --sky-bottom: #d8b18e;
    --lawn: #4e6b3a;
  }
  html, body {
    margin: 0;
    padding: 0;
    width: 850px;
    height: 1200px;
    overflow: hidden;
    background: var(--paper);
  }
  .flyer {
    position: relative;
    width: 850px;
    height: 1200px;
    background: var(--paper);
    font-family: "Open Sans", Arial, sans-serif;
    color: var(--white);
  }

  /* Hero */
  .hero-photo {
    position: absolute;
    left: 33px; top: 46px;
    width: 507px; height: 497px;
    background: radial-gradient(ellipse at 45% 30%, var(--photo-red-light) 0%, var(--brand-red) 45%, var(--photo-red-dark) 100%);
  }
  .hero-tagline {
    position: absolute;
    left: 81px; top: 352px;
    margin: 0;
    font-family: "Open Sans", Arial, sans-serif;
    font-weight: 400;
    font-size: 29px;
    line-height: 1.2;
    color: var(--white);
  }
  .hero-headline {
    position: absolute;
    left: 81px; top: 394px;
    margin: 0;
    font-family: "Montserrat", Arial, sans-serif;
    font-weight: 800;
    font-size: 47px;
    line-height: 58px;
    text-transform: uppercase;
    color: var(--white);
  }

  /* Brand */
  .brand {
    position: absolute;
    left: 540px; top: 46px;
    width: 271px; height: 296px;
    display: flex;
    flex-direction: column;
    align-items: center;
    justify-content: center;
    gap: 22px;
  }
  .brand-mark {
    width: 52px; height: 52px;
    background: var(--brand-red);
  }
  .brand-name {
    margin: 0;
    font-family: "Montserrat", Arial, sans-serif;
    font-weight: 700;
    font-size: 28px;
    line-height: 38px;
    text-align: center;
    color: var(--ink);
  }

  .listing-photo {
    position: absolute;
    left: 540px; top: 342px;
    width: 271px; height: 195px;
    background: linear-gradient(180deg, var(--sky-top) 0%, var(--sky-bottom) 70%, var(--lawn) 100%);
  }

  /* Quote band */
  .quote-band {
    position: absolute;
    left: 33px; top: 539px;
    width: 778px; height: 118px;
    background: var(--ink);
  }
  .quote-text {
    position: absolute;
    left: 62px; top: 25px;
    width: 680px;
    margin: 0;
    font-size: 16px;
    line-height: 22px;
    color: var(--white);
  }
  .quote-mark {
    font-family: "Montserrat", Arial, sans-serif;
    font-weight: 800;
    color: var(--brand-red);
    font-size: 58px;
    line-height: 0;
    vertical-align: -22px;
    letter-spacing: -4px;
  }
  .quote-mark--open { margin-right: 8px; margin-left: -20px; }
  .quote-mark--close { margin-left: 8px; }

  /* Offer */
  .offer-shape {
    position: absolute;
    left: 0; top: 0;
    width: 850px; height: 1200px;
  }
  .offer-title {
    position: absolute;
    left: 422px; top: 744px;
    margin: 0;
    font-family: "Montserrat", Arial, sans-serif;
    font-weight: 700;
    font-size: 23px;
    line-height: 32px;
    text-transform: uppercase;
    color: var(--white);
  }
  .offer-body {
    position: absolute;
    left: 422px; top: 832px;
    width: 352px;
    margin: 0;
    font-size: 15.5px;
    line-height: 22px;
    color: var(--white);
  }

  .features {
    position: absolute;
    left: 75px; top: 822px;
    margin: 0;
  }
  .features-title {
    margin: 0 0 2px;
    font-family: "Montserrat", Arial, sans-serif;
    font-weight: 700;
    font-size: 20px;
    line-height: 28px;
    text-transform: uppercase;
    color: var(--brand-red);
  }
  .features-list {
    margin: 0;
    padding: 0;
    list-style: none;
    font-family: "Montserrat", Arial, sans-serif;
    font-weight: 600;
    font-size: 20px;
    line-height: 27px;
    color: var(--ink);
  }
  .features-list li::before {
    content: "•";
    margin-right: 8px;
  }

  /* Footer */
  .agent-name {
    position: absolute;
    left: 33px; top: 1040px;
    width: 350px; height: 107px;
    margin: 0;
    display: flex;
    align-items: center;
    justify-content: center;
    background: var(--brand-red);
    font-family: "Montserrat", Arial, sans-serif;
    font-weight: 600;
    font-size: 33px;
    color: var(--white);
  }
  .agent-contact {
    position: absolute;
    left: 383px; top: 1040px;
    width: 428px; height: 107px;
    display: flex;
    flex-direction: column;
    align-items: center;
    justify-content: center;
    background: var(--ink);
    font-family: "Montserrat", Arial, sans-serif;
    color: var(--white);
  }
  .agent-phone {
    font-weight: 700;
    font-size: 35px;
    line-height: 42px;
  }
  .agent-email {
    font-weight: 600;
    font-size: 19px;
    line-height: 26px;
  }
</style>
</head>
<body>
<main class="flyer">

  <div class="hero-photo" role="img" aria-label="Photo of a smiling young family sitting on the floor of their new home, toned in brand red"></div>
  <p class="hero-tagline">a right choice for</p>
  <h1 class="hero-headline">Your big<br>dreams</h1>

  <div class="brand">
    <span class="brand-mark" aria-hidden="true"></span>
    <p class="brand-name">KESTON<br>REALTY</p>
  </div>

  <div class="listing-photo" role="img" aria-label="Photo of a two-storey suburban house with a garage and front lawn at dusk"></div>

  <section class="quote-band">
    <p class="quote-text"><span class="quote-mark quote-mark--open">“</span>Lorem Ipsum is simply dummy text of the printing and typesetting industry. Lorem Ipsum has been the industry's standard dummy text ever since the 1500s, when an unknown printer took a galley of type and scramb<span class="quote-mark quote-mark--close">”</span></p>
  </section>

  <svg class="offer-shape" viewBox="0 0 850 1200" aria-hidden="true">
    <polygon points="154,657 811,657 811,1040 383,1040 383,884" fill="var(--brand-red)"/>
  </svg>

  <section class="offer">
    <h2 class="offer-title">Elegant homes for sale<br>$ 2,500,000</h2>
    <p class="offer-body">Lorem Ipsum is simply dummy text of the printing and typesetting industry. Lorem Ipsum has been the industry's standard dummy text ever since the 1500s, when an unknown printer took a galley of type and scrambled it to make a type specimen book. It has survived not only five centuries, but also the leap into electronic typesetting, remaining essentiall</p>
  </section>

  <section class="features">
    <h3 class="features-title">Awesome features</h3>
    <ul class="features-list">
      <li>4 Bedroom</li>
      <li>Kitchen Room</li>
      <li>Guest Room</li>
      <li>Laundry Room</li>
      <li>2 Living Room</li>
      <li>Swimming Pool</li>
    </ul>
  </section>

  <footer>
    <p class="agent-name">JORDAN KESTON</p>
    <div class="agent-contact">
      <span class="agent-phone">555-204-0187</span>
      <span class="agent-email">JKESTON@EXAMPLE.COM</span>
    </div>
  </footer>

</main>
</body>
</html>
```